KO-TRA , Artificial hedge flyer

i need new flyer, in att i'm sending old one but as we produce artificial flowers, trees and most popular is artificial green hedge, and it's used from variety places, from swimming pool, restaurants, bars, private terrace, gardens, to protect from neighbor :-) . from beginning is all our product, it's not imported from other producer. we are doing it by measure what we get from customer ( tailor made ) , we give guaranty 15-20 years on all weather that will not loos color, etc.. you can see some pictures in att on old flyer, and some new pictures of same in space newly added. we'd like more pictures with samples of use, etc.you can see our product on www.ko-tra.hr so you can closely known what we are producing, and what for we need new flyer. we have plenty of new picture that are not on our web, so i can use it for new flyer.

Font styles to use
Sans Serif

Requirements
Must have
• company logo, contact info ( sent in word document in att ), logo of croatian product ( on old flyer in att on front side), stamp Quality since 1950 if you could change year to 1960, last time they made mistake and write 1950 ),
Nice to have
• flyer 3 fold type, or if you think it will look better only double side flyer, depend of design and theme so everyone can understand what is our business

```html
<!DOCTYPE html>
<html lang="hr">
<head>
<meta charset="utf-8">
<title>KO-TRA – letak</title>
<link rel="stylesheet" href="https://fonts.googleapis.com/css2?family=Montserrat:wght@400;500;600;700;800&display=swap">
<style>
  :root{
    --green:#2fa84f;
    --green-dark:#1d7a36;
    --green-light:#8fd14f;
    --ink:#4a4a4a;
    --grey:#8a8a8a;
    --paper:#ffffff;
    --bg:#eef0ee;
  }
  html,body{margin:0;padding:0;overflow:hidden;}
  body{width:1200px;height:2468px;background:var(--bg);font-family:"Montserrat",sans-serif;position:relative;}
  .flyer-side{position:absolute;left:40px;width:1120px;height:720px;background:var(--paper);box-shadow:0 6px 24px rgba(0,0,0,.12);}
  .flyer-side--outer{top:454px;}
  .flyer-side--inner{top:1294px;}
  .flyer-side svg{display:block;width:1120px;height:720px;}
  .t-title{font-family:"Montserrat",sans-serif;font-weight:800;fill:var(--ink);}
  .t-title--green{fill:var(--green);}
  .t-body{font-family:"Montserrat",sans-serif;font-weight:500;fill:var(--ink);}
  .t-caps{font-family:"Montserrat",sans-serif;font-weight:700;fill:var(--green);letter-spacing:.5px;}
  .t-web{font-family:"Montserrat",sans-serif;font-weight:700;fill:var(--green);}
  .t-white{fill:#fff;}
  .brand-name{font-family:"Montserrat",sans-serif;font-weight:700;fill:var(--green-dark);}
  .icon-dot{fill:var(--green);}
  .curve{fill:none;stroke:var(--green);}
</style>
</head>
<body>

<section class="flyer-side flyer-side--outer" aria-label="Vanjska strana letka">
<svg viewBox="0 0 1120 720" xmlns="http://www.w3.org/2000/svg">
  <defs>
    <linearGradient id="pool" x1="0" y1="0" x2="0" y2="1">
      <stop offset="0" stop-color="#6b6f63"/><stop offset=".5" stop-color="#8a8f82"/><stop offset="1" stop-color="#3f8fb3"/>
    </linearGradient>
    <linearGradient id="deck" x1="0" y1="0" x2="1" y2="1">
      <stop offset="0" stop-color="#5e7a4a"/><stop offset=".45" stop-color="#a0552e"/><stop offset="1" stop-color="#7a3a1c"/>
    </linearGradient>
    <radialGradient id="garden" cx=".5" cy=".4" r=".6">
      <stop offset="0" stop-color="#b8c7b0"/><stop offset="1" stop-color="#4f7a3a"/>
    </radialGradient>
    <clipPath id="circleGarden"><circle cx="930" cy="175" r="150"/></clipPath>
  </defs>

  <rect class="photo" role="img" aria-label="Fotografija terase s bazenom i umjetnom živicom" x="0" y="0" width="760" height="330" fill="url(#pool)"/>
  <path d="M0 300 C 200 250, 420 360, 760 250 L760 330 L0 330 Z" fill="#fff"/>
  <path class="curve" d="M0 300 C 200 250, 420 360, 760 250" stroke-width="8"/>
  <path class="curve" d="M0 318 C 220 275, 430 380, 780 268" stroke-width="3" stroke="var(--green-light)"/>

  <circle cx="930" cy="175" r="158" fill="var(--green)"/>
  <rect role="img" aria-label="Fotografija vrta s suncobranom i živicom" x="770" y="10" width="320" height="320" fill="url(#garden)" clip-path="url(#circleGarden)"/>
  <circle cx="812" cy="36" r="10" fill="var(--green)"/>
  <text class="brand-name" x="830" y="46" font-size="28">KO-TRA d.o.o.</text>

  <path d="M0 360 L340 360 C 400 480, 380 620, 320 720 L0 720 Z" role="img" aria-label="Fotografija drvene terase s ležaljkama" fill="url(#deck)"/>
  <path class="curve" d="M340 360 C 400 480, 380 620, 320 720" stroke-width="8"/>

  <rect x="410" y="350" width="160" height="30" rx="15" fill="var(--green)"/>
  <text class="t-caps t-white" x="490" y="371" font-size="15" text-anchor="middle">CONTACT US</text>
  <g class="contact">
    <circle class="icon-dot" cx="440" cy="420" r="14"/>
    <path d="M434 413 l4 0 l2 5 l-2 2 a10 10 0 0 0 5 5 l2-2 l5 2 l0 4 a2 2 0 0 1 -2 2 a18 18 0 0 1 -16 -16 a2 2 0 0 1 2 -2z" fill="#fff"/>
    <text class="t-body" x="465" y="416" font-size="13">+385 00 000 000</text>
    <text class="t-body" x="465" y="434" font-size="13">+385 00 000 001</text>
    <circle class="icon-dot" cx="440" cy="490" r="14"/>
    <path d="M440 480 a7 7 0 0 1 7 7 c0 5 -7 12 -7 12 c0 0 -7 -7 -7 -12 a7 7 0 0 1 7 -7z" fill="#fff"/>
    <text class="t-body" x="465" y="486" font-size="13">Zelena ulica 22</text>
    <text class="t-body" x="465" y="504" font-size="13">10000 Zagreb</text>
    <circle class="icon-dot" cx="440" cy="560" r="14"/>
    <rect x="432" y="554" width="16" height="12" fill="none" stroke="#fff" stroke-width="2"/>
    <path d="M432 555 l8 6 l8 -6" fill="none" stroke="#fff" stroke-width="2"/>
    <text class="t-body" x="465" y="565" font-size="13">info@ko-tra.hr</text>
    <circle class="icon-dot" cx="440" cy="630" r="14"/>
    <circle cx="440" cy="630" r="7" fill="none" stroke="#fff" stroke-width="2"/>
    <text class="t-body" x="465" y="635" font-size="13">www.ko-tra.hr</text>
  </g>

  <text class="t-title" x="770" y="400" font-size="40">UNUTARNJE I</text>
  <text class="t-title" x="770" y="446" font-size="40" fill-opacity=".8">VANJSKO</text>
  <text class="t-title" x="770" y="492" font-size="40">UREĐENJE</text>
  <text class="t-caps" x="770" y="525" font-size="11">UMJETNA ŽIVICA PO MJERI, CVIJEĆE I STABLA</text>
  <text class="t-caps" x="770" y="541" font-size="11">ZA BAZENE, RESTORANE, TERASE I VRTOVE</text>
  <text class="t-caps" x="770" y="557" font-size="11">DOMAĆI PROIZVOD, JAMSTVO 15–20 GODINA</text>
  <circle cx="930" cy="612" r="30" fill="none" stroke="var(--grey)" stroke-width="3"/>
  <circle cx="930" cy="612" r="22" fill="var(--grey)" fill-opacity=".35"/>
  <text class="t-web" x="1090" y="690" font-size="22" text-anchor="end">www.ko-tra.hr</text>
</svg>
</section>

<section class="flyer-side flyer-side--inner" aria-label="Unutarnja strana letka">
<svg viewBox="0 0 1120 720" xmlns="http://www.w3.org/2000/svg">
  <defs>
    <linearGradient id="tree" x1="0" y1="0" x2="0" y2="1">
      <stop offset="0" stop-color="#3f5a36"/><stop offset=".55" stop-color="#5f8a3e"/><stop offset="1" stop-color="#b9b3a6"/>
    </linearGradient>
    <linearGradient id="patio" x1="0" y1="0" x2="1" y2="0">
      <stop offset="0" stop-color="#7f8a77"/><stop offset=".6" stop-color="#c9c6bd"/><stop offset="1" stop-color="#5d8a44"/>
    </linearGradient>
    <radialGradient id="arbor" cx=".5" cy=".5" r=".6">
      <stop offset="0" stop-color="#c9b08a"/><stop offset="1" stop-color="#4e7d38"/>
    </radialGradient>
    <clipPath id="circleArbor"><circle cx="990" cy="400" r="105"/></clipPath>
  </defs>

  <rect role="img" aria-label="Fotografija terase s umjetnim stablom i živicom" x="0" y="0" width="1120" height="360" fill="url(#patio)"/>
  <path d="M0 0 L420 0 L420 720 L0 720 Z" role="img" aria-label="Fotografija umjetnog stabla u posudi" fill="url(#tree)"/>
  <path d="M420 360 C 600 300, 800 400, 1120 300 L1120 720 L420 720 Z" fill="#fff"/>
  <path class="curve" d="M420 360 C 600 300, 800 400, 1120 300" stroke-width="8"/>
  <path class="curve" d="M420 382 C 600 322, 820 420, 1120 322" stroke-width="3" stroke="var(--green-light)"/>

  <circle cx="990" cy="400" r="112" fill="var(--green)"/>
  <rect role="img" aria-label="Fotografija vrtne sjenice sa živicom" x="880" y="290" width="220" height="220" fill="url(#arbor)" clip-path="url(#circleArbor)"/>

  <text class="t-title" x="450" y="470" font-size="28" font-weight="700">Unutarnje i vanjsko</text>
  <text class="t-title" x="450" y="505" font-size="28" font-weight="700">uređenje prostora</text>
  <g class="service-list">
    <circle class="icon-dot" cx="462" cy="552" r="9"/>
    <text class="t-body" x="482" y="557" font-size="15">Umjetnom živicom</text>
    <circle class="icon-dot" cx="462" cy="588" r="9"/>
    <text class="t-body" x="482" y="593" font-size="15">Stablima</text>
    <circle class="icon-dot" cx="462" cy="624" r="9"/>
    <text class="t-body" x="482" y="629" font-size="15">Dekorativnim lišćem</text>
    <text class="t-body" x="482" y="647" font-size="15">i cvijećem</text>
  </g>
  <text class="t-web" x="450" y="690" font-size="14">www.ko-tra.hr</text>

  <text class="t-body" x="870" y="570" font-size="16" font-weight="600">Zelena ulica 22</text>
  <text class="t-body" x="870" y="592" font-size="16" font-weight="600">10000 Zagreb</text>
  <circle class="icon-dot" cx="880" cy="640" r="10"/>
  <text class="t-body" x="898" y="645" font-size="14">+385 00 000 000</text>
</svg>
</section>

</body>
</html>
```